EPIC, awesome, creative business card needed - get involved!

I'm launching a boutique, exclusive Property Management real estate agency in Sydney early next year.
The name of the agency will be called "Quartz Hill Lane" - it's a play on "chase the silver pebble trail" to wealth. The Quartz Hill Lane signifies wealth through property investment.
My business will offer management of investment properties (ie Property Management).
The difference with Quartz Hill Lane and other agencies is the business will be run by one of Australia's leading property investment experts, and also one of Australia's leading property managers.
It will be exclusively for high net worth properties and individuals, so the business card needs to be extremely sharp, slick and relatively simple.
The information I want on the card is as follows
Nolan Pryce - Director
M: 0412 967 154
P: 9735 6021
E: nolan@quartzhilllane.net.au
W: quartzhilllane.net.au
I'm happy with the red from the logo, black - no yellows or funky colors. I want this to be a super corporate and slick business card to match the high end nature of the business.
Good luck everyone, and please ask questions for clarification.

```html
<!DOCTYPE html>
<html lang="en">
<head>
<meta charset="utf-8">
<title>Quartz Hill Lane – Business Card</title>
<link rel="stylesheet" href="https://fonts.googleapis.com/css2?family=Exo+2:wght@300;400&display=swap">
<style>
  :root {
    --brand-red: #c8000a;
    --band-red: #d91a04;
    --band-orange: #e8480a;
    --glow: #f26a3a;
    --white: #ffffff;
    --rule: rgba(150, 0, 0, 0.35);
    --map-light: #ff9a80;
    --map-mid: #ff5a48;
  }
  html, body {
    margin: 0;
    width: 1200px;
    height: 1000px;
    overflow: hidden;
    background: var(--white);
    font-family: "Exo 2", sans-serif;
  }
  .canvas { position: relative; width: 1200px; height: 1000px; }

  .card {
    position: absolute;
    width: 556px;
    height: 318px;
    overflow: hidden;
    box-shadow: 4px 4px 6px rgba(0, 0, 0, 0.45);
  }

  /* Front */
  .card--front {
    left: 136px; top: 122px;
    background: var(--white);
    outline: 1px solid #d6d6d6;
  }
  .front__band {
    position: absolute; left: 0; top: 123px; width: 100%; height: 195px;
    background: linear-gradient(135deg, var(--band-red) 0%, #dc2a04 55%, var(--band-orange) 100%);
  }
  .frame-line { position: absolute; background: var(--white); }
  .front__band .frame-line--top { left: 0; right: 0; top: 13px; height: 3px; }
  .front__band .frame-line--bottom { left: 0; right: 0; bottom: 8px; height: 3px; }
  .front__band .frame-line--left { top: 0; bottom: 0; left: 6px; width: 3px; }
  .front__band .frame-line--right { top: 0; bottom: 0; right: 8px; width: 3px; }

  .map-area {
    position: absolute; left: 318px; top: 18px; width: 214px; height: 212px;
    border-radius: 38% 46% 40% 30% / 30% 36% 52% 50%;
    background: linear-gradient(135deg, var(--map-mid) 0%, var(--map-light) 45%, var(--map-mid) 100%);
    opacity: 0.9;
  }

  .brand { position: absolute; display: flex; align-items: center; }
  .brand__mark { border-radius: 50%; flex: none; }
  .brand__name { font-weight: 300; white-space: nowrap; line-height: 1; }

  .card--front .brand { left: 13px; top: 34px; z-index: 1; }
  .card--front .brand__mark { width: 72px; height: 72px; background: var(--brand-red); margin-right: 16px; }
  .card--front .brand__name { font-size: 26px; color: var(--brand-red); }

  .contact {
    position: absolute; left: 21px; top: 160px;
    margin: 0; padding: 0; list-style: none;
    color: var(--white); font-size: 13px; font-weight: 400;
  }
  .contact li { height: 27px; line-height: 20px; border-bottom: 1px solid var(--rule); }
  .contact li:nth-child(1) { width: 278px; }
  .contact li:nth-child(2) { width: 308px; }
  .contact li:nth-child(3) { width: 330px; }
  .contact li:nth-child(4) { width: 352px; }
  .contact li:nth-child(5) { border-bottom: none; }

  /* Back */
  .card--back {
    left: 342px; top: 497px;
    background:
      radial-gradient(circle at 145px 155px, var(--glow) 0%, #ea4a1c 18%, #e03a08 36%, transparent 62%),
      linear-gradient(90deg, #e03a06 0%, var(--band-red) 60%, var(--brand-red) 100%);
  }
  .card--back .frame-line--top { left: 0; right: 0; top: 11px; height: 6px; }
  .card--back .frame-line--bottom { left: 0; right: 0; bottom: 12px; height: 6px; }
  .card--back .frame-line--left { top: 0; bottom: 0; left: 13px; width: 6px; }
  .card--back .frame-line--right { top: 0; bottom: 0; right: 15px; width: 6px; }

  .card--back .brand { left: 98px; top: 109px; }
  .card--back .brand__mark { width: 92px; height: 92px; background: var(--white); margin-right: 20px; }
  .card--back .brand__name { font-size: 34px; color: var(--white); }
  .back__rule {
    position: absolute; left: 100px; top: 211px; width: 356px; height: 1px;
    background: rgba(160, 20, 0, 0.45);
  }
</style>
</head>
<body>
<main class="canvas">
  <section class="card card--front" aria-label="Business card front">
    <div class="front__band">
      <span class="frame-line frame-line--top"></span>
      <span class="frame-line frame-line--bottom"></span>
      <span class="frame-line frame-line--left"></span>
      <span class="frame-line frame-line--right"></span>
    </div>
    <div class="map-area" role="img" aria-label="Map of Australia in soft red gradient"></div>
    <div class="brand">
      <span class="brand__mark"></span>
      <span class="brand__name">Quartz Hill Lane</span>
    </div>
    <ul class="contact">
      <li>Nolan Pryce – Director</li>
      <li>M: 0412 967 154</li>
      <li>P: 9735 6021</li>
      <li>E: nolan@quartzhilllane.net.au</li>
      <li>W: quartzhilllane.net.au</li>
    </ul>
  </section>

  <section class="card card--back" aria-label="Business card back">
    <span class="frame-line frame-line--top"></span>
    <span class="frame-line frame-line--bottom"></span>
    <span class="frame-line frame-line--left"></span>
    <span class="frame-line frame-line--right"></span>
    <div class="brand">
      <span class="brand__mark"></span>
      <span class="brand__name">Quartz Hill Lane</span>
    </div>
    <span class="back__rule"></span>
  </section>
</main>
</body>
</html>
```